Brierley Dunmore Lawyers needs a web design

We need a web design for our conveyancing and commercial law firm based in Sydney Australia. We want to depersonalise the current website: http://www.brierleydunmore.example/ and give it a classic modern feel to it. It should be a simple design (possibly one page) and communicate trust, professionalism and experience.

Content should include:

Brierley Dunmore is a boutique Sydney based legal practice specialising in business and property law.

We pride ourselves on our proactive, receptive and dynamic approach to client service. Our business survives on referrals from satisfied clients and professionals who respect the way we do business.

Practice areas

Business law

We act on the sale and purchase of businesses. We assist clients with structuring their businesses, drafting shareholder agreements and buy-sell arrangements. We have acted on a multitude of other commercial matters including franchising, distribution, marketing and business services (with a particular focus in the advertising sector).

Property law

We act for developers, commercial property investors, landlords and tenants. We also handle residential conveyancing and deal with strata and company title matters.

Private Client

We draft wills and codicils on behalf of clients and can also assist with applications for probate should the need arise.

Contact Us

Brierley Dunmore
Level 29, Wexcombe Tower
7 Marlowe Square
Sydney, NSW 2000

t: +61 (0)2 9471 6203
f: +61 (0)2 8526 4079
e: enquiries@brierleydunmore.example

Target Market(s)

Individuals and business who need legal advice in the area of property and commercial law

Industry/Entity Type

Legal

Number of Pages Required

1 page

Font styles to use
Sans Serif

Requirements
Must have
• Clear and concise content.
Nice to have
• Some images to break up the content.
Should not have
• Any offensive images tones or connotations.

```html
<!DOCTYPE html>
<html lang="en">
<head>
<meta charset="utf-8">
<title>Brierley Dunmore Lawyers</title>
<link rel="stylesheet" href="https://fonts.googleapis.com/css2?family=Roboto:wght@300;400;500&family=Noto+Serif:wght@400&display=swap">
<style>
:root{
  --navy:#0b2f7a;
  --navy-dark:#082a6e;
  --grey-text:#6b6b6b;
  --dark-text:#222;
  --light-bg:#f3f3f3;
  --footer-bg:#2b2b2b;
  --footer-text:#bdbdbd;
  --white:#fff;
  --line:#cfcfcf;
}
*{margin:0;padding:0;box-sizing:border-box}
html,body{width:966px;height:1200px;overflow:hidden;background:var(--white)}
body{position:relative;font-family:'Roboto',sans-serif;color:var(--dark-text)}
.site-header{position:absolute;left:0;top:0;width:966px;height:82px;background:var(--white)}
.brand{position:absolute;left:78px;top:16px;color:var(--navy);font-weight:300;line-height:1}
.brand-name{display:block;font-size:27px}
.brand-sub{display:block;font-size:13px;text-align:right;margin-top:4px}
.main-nav a{position:absolute;top:32px;font-size:11px;color:var(--grey-text);text-decoration:none;font-weight:300}
.main-nav a.active{color:var(--navy);font-weight:400}
.hero{position:absolute;left:0;top:82px;width:966px;height:332px;
  background:linear-gradient(100deg,#2b2d33 0%,#5a5d63 18%,#d9d6d2 40%,#eceae8 62%,#e6e3df 80%,#8a6a44 92%,#cfcbc6 100%)}
.hero-arrow{position:absolute;top:152px;width:21px;height:27px;background:rgba(60,60,60,.75)}
.hero-arrow.prev{left:0}
.hero-arrow.next{right:0}
.hero-arrow svg{display:block;margin:6px auto}
.services{position:absolute;left:0;top:414px;width:966px;height:143px;background:var(--navy-dark)}
.service{position:absolute;top:35px;color:var(--white)}
.service-icon{position:absolute;left:0;top:0;width:69px;height:69px;border-radius:50%;background:var(--white);display:flex;align-items:center;justify-content:center}
.service h2{position:absolute;left:78px;top:-3px;font-size:18.5px;font-weight:400;white-space:nowrap}
.service p{position:absolute;left:79px;top:24px;width:160px;font-size:7.8px;line-height:12.4px;font-weight:300;color:#dfe6f3}
.welcome{position:absolute;left:0;top:557px;width:966px;height:243px;text-align:center}
.welcome h1{position:absolute;left:0;width:100%;top:45px;font-size:24px;font-weight:500;color:var(--navy)}
.welcome .lead{position:absolute;left:0;width:100%;top:92px;font-size:10.5px;color:var(--dark-text)}
.welcome .intro{position:absolute;left:138px;width:690px;top:116px;font-size:9px;line-height:15px;color:var(--grey-text)}
.btn-contact{position:absolute;left:438px;top:161px;width:91px;height:35px;border:1px solid var(--line);font-size:9.5px;color:var(--grey-text);line-height:33px;letter-spacing:.3px}
.testimonials{position:absolute;left:0;top:800px;width:966px;height:242px;background:var(--light-bg);text-align:center}
.testimonials h2{position:absolute;left:0;width:100%;top:37px;font-size:20.5px;font-weight:400;color:var(--navy)}
.quote{position:absolute;left:172px;width:622px;top:76px;font-size:10.5px;line-height:19px;color:var(--grey-text)}
.quote .mark{font-family:'Noto Serif',serif;font-size:24px;color:#555;line-height:0;vertical-align:-6px;font-weight:700}
.client-name{position:absolute;left:0;width:100%;top:149px;font-size:12px;color:var(--dark-text)}
.client-company{position:absolute;left:0;width:100%;top:168px;font-size:8.5px;color:var(--grey-text)}
.dots{position:absolute;left:457px;top:198px;display:flex;gap:11px}
.dots span{width:9px;height:9px;border-radius:50%;border:1px solid #bbb;background:var(--white)}
.dots span.on{background:radial-gradient(circle,#aaa 0 2px,var(--white) 2.5px)}
.contact-bar{position:absolute;left:0;top:1042px;width:966px;height:76px;font-family:'Noto Serif',serif;font-size:8px;color:var(--grey-text)}
.contact-item{position:absolute;top:32px;display:flex;align-items:center;gap:6px;white-space:nowrap}
.site-footer{position:absolute;left:0;top:1118px;width:966px;height:82px;background:var(--footer-bg);color:var(--footer-text);font-size:8.5px}
.footer-nav{position:absolute;left:80px;top:24px}
.footer-nav a{color:var(--footer-text);text-decoration:none}
.footer-nav .sep{margin:0 6px}
.copyright{position:absolute;left:80px;top:46px}
.social{position:absolute;left:804px;top:30px;display:flex;gap:9px}
.social span{width:21px;height:21px;border-radius:50%}
.social .s1{background:#3b5998}.social .s2{background:#29a9e1}.social .s3{background:#1e88b8}
</style>
</head>
<body>
<header class="site-header">
  <div class="brand"><span class="brand-name">Brierley Dunmore</span><span class="brand-sub">Lawyers</span></div>
  <nav class="main-nav">
    <a class="active" href="#" style="left:518px">Home</a>
    <a href="#" style="left:574px">Our Profile</a>
    <a href="#" style="left:650px">Practice Areas</a>
    <a href="#" style="left:745px">Terstimonials</a>
    <a href="#" style="left:836px">Contact us</a>
  </nav>
</header>

<section class="hero" role="img" aria-label="Lawyer in a dark suit stamping a document at a desk beside a bronze statue of Justice">
  <div class="hero-arrow prev"><svg width="9" height="15" viewBox="0 0 9 15"><path d="M8 1L1 7.5 8 14" fill="none" stroke="#fff" stroke-width="1.2"/></svg></div>
  <div class="hero-arrow next"><svg width="9" height="15" viewBox="0 0 9 15"><path d="M1 1l7 6.5L1 14" fill="none" stroke="#fff" stroke-width="1.2"/></svg></div>
</section>

<section class="services">
  <div class="service" style="left:80px">
    <div class="service-icon"><svg width="30" height="26" viewBox="0 0 30 26"><path d="M10 5V2h10v3" fill="none" stroke="#0b2f7a" stroke-width="2.4"/><rect x="1" y="5" width="28" height="20" rx="2" fill="#0b2f7a"/><rect x="1" y="13" width="28" height="1.6" fill="#fff"/><rect x="12.5" y="11.5" width="5" height="4.5" fill="#fff"/><rect x="13.7" y="12.7" width="2.6" height="2" fill="#0b2f7a"/></svg></div>
    <h2>Business Law</h2>
    <p>We act on the sale and purchase of busi-nesses. We assist clients with structuring their businesses, drafting shareholder agreements and buy-sell arrangements.</p>
  </div>
  <div class="service" style="left:367px">
    <div class="service-icon"><svg width="30" height="26" viewBox="0 0 30 26"><path d="M15 2L1 14h4v11h7v-7h6v7h7V14h4z" fill="#0b2f7a"/><rect x="21" y="3" width="3.5" height="6" fill="#0b2f7a"/></svg></div>
    <h2>Property law</h2>
    <p>We act for developers, commercial proper-ty investors, landlords and tenants. We also handle residential conveyancing and deal with strata and company title matters.</p>
  </div>
  <div class="service" style="left:660px">
    <div class="service-icon"><svg width="28" height="28" viewBox="0 0 28 28"><circle cx="14" cy="8" r="6.5" fill="#0b2f7a"/><path d="M2 27v-4c0-5 4-8 9-8h6c5 0 9 3 9 8v4z" fill="#0b2f7a"/></svg></div>
    <h2>Private Client</h2>
    <p>We draft wills and codicils on behalf of clients and can also assist with applica-tions for probate should the need arise.</p>
  </div>
</section>

<section class="welcome">
  <h1>Welcome to BrierleyDunmore</h1>
  <p class="lead">Brierley Dunmore is a boutique Sydney based legal practice specialising in business and property law.</p>
  <p class="intro">We pride ourselves on our proactive, receptive and dynamic approach to client service. Our business survives on referrals from satisfied clients and professionals who respect the way we do business.</p>
  <div class="btn-contact">CONTACT US</div>
</section>

<section class="testimonials">
  <h2>Client’s Testimonials</h2>
  <p class="quote"><span class="mark">“</span> Aliquam erat volutpat. Etiam quis aliquet risus. Duis ornare erat eget magna dapibus, in accumsan quam pharetra. Nam tempus, quam in bibendum vulputate, sapien dolor viverra nisl, vitae euismod elit turpis et nulla. Aliquam erat volutpat. Pellen-tesque blandit lacus eget nunc faucibus, et tincidunt eros viverra. <span class="mark">”</span></p>
  <p class="client-name">Alan Pryce</p>
  <p class="client-company">Company name</p>
  <div class="dots"><span class="on"></span><span></span><span></span></div>
</section>

<section class="contact-bar">
  <div class="contact-item" style="left:84px"><svg width="8" height="11" viewBox="0 0 8 11"><path d="M4 0a4 4 0 0 0-4 4c0 3 4 7 4 7s4-4 4-7a4 4 0 0 0-4-4z" fill="#777"/><circle cx="4" cy="4" r="1.5" fill="#fff"/></svg>Level 29, Wexcombe Tower, 7 Marlowe Square, Sydney, NSW 2000</div>
  <div class="contact-item" style="left:391px"><svg width="10" height="10" viewBox="0 0 10 10"><path d="M2 0l2 2.5-1.2 1.3a6 6 0 0 0 3.4 3.4L7.5 6 10 8 8.5 10C4 10 0 6 0 1.5z" fill="#777"/></svg>Phone: +61 (0)2 9471 6203</div>
  <div class="contact-item" style="left:550px"><svg width="11" height="10" viewBox="0 0 11 10"><rect x="0" y="3" width="11" height="7" fill="#777"/><rect x="3" y="0" width="6" height="4" fill="#777"/><rect x="4" y="5" width="5" height="3" fill="#fff"/></svg>Fax: +61 (0)2 8526 4079</div>
  <div class="contact-item" style="left:699px"><svg width="11" height="8" viewBox="0 0 11 8"><rect width="11" height="8" fill="#777"/><path d="M0 0l5.5 4.5L11 0" fill="none" stroke="#fff" stroke-width="1"/></svg>E-mail : enquiries@brierleydunmore.example</div>
</section>

<footer class="site-footer">
  <nav class="footer-nav"><a href="#">Home</a><span class="sep">|</span><a href="#">Our Profile</a><span class="sep">|</span><a href="#">Practice Areas</a><span class="sep">|</span><a href="#">Terstimonials</a><span class="sep">|</span><a href="#">Contact us</a></nav>
  <p class="copyright">Copyright &nbsp;©&nbsp; 2015 &nbsp;BrierleyDunmore. All rights reserved</p>
  <div class="social"><span class="s1"></span><span class="s2"></span><span class="s3"></span></div>
</footer>
</body>
</html>
```